Web Design Project for Kurbly, Chicago

We require a Website designed for a new application. Kurbly, a street parking application which helps car drivers find a street parking spot by offering an ideal path along which to look for parking. This path is calculated by our algorithm based on data (e.g. historical data, baseball games schedule, etc.). Along this path the driver will find a spot and will also save 70% of the search time. Customer we target is reg. between 21 and 45 yo.

We'd like the website to be based on the structure of the attached PDF. Could also be totally different and creative. Open to other options!!!
WE LIKE THIS PAGE: http://www.trelvoqa.de/

We require the following pages designed:
- Main/Home page; with the app demo and maybe a blog implemented on the side
- About page (for company and team)
- Contact page,
- Cool link to get app
- Link for Press/Blog/Socal Media integration and Privacy Policy

Supplied as layered PSD Files

For reference/inspiration only:
One page we like is vornitel.com
Good widget page design: platemerio.com/widgets
Also like their blog: platemerio.com/blog
(Note chirplet integration on the right hand side, as well as Meet the Team video)

Reason: We're starting to get more and more designs and need more time to look into all of them. Very exciting!! Thanks to everybody!

Hi all, we are reviewing the submitted designs and will add some updates to the brief shortly. Sorry about the delay but it's very hard to pick from all those great ideas. Cheers

Target Market(s)

Young, trendy look and interested in tech!

Industry/Entity Type

Parking

Requirements
Must have
• Map should show a path like the app does. Examples to be found under appvista shop Kurbly
Please put the widget as a link and not with a big picture.

```html
<!DOCTYPE html>
<html lang="en">
<head>
<meta charset="utf-8">
<title>Kurbly – Widget</title>
<link rel="stylesheet" href="https://fonts.googleapis.com/css2?family=Archivo+Black&family=Arimo:wght@400;700&family=Cousine&display=swap">
<style>
:root{
  --ground:#e3e3e3;
  --ground-deep:#bdbdbd;
  --panel:#ffffff;
  --side:#ecebe8;
  --ink:#2b2b2b;
  --muted:#555555;
  --nav:#355a57;
  --brand-blue:#1f7fd0;
  --map:#ebe8e1;
}
*{box-sizing:border-box;margin:0;padding:0}
html,body{width:1200px;height:900px;overflow:hidden}
body{position:relative;background:var(--ground);font-family:"Arimo",Arial,sans-serif;color:var(--ink)}
.scenery{position:absolute;inset:0;background:linear-gradient(180deg,var(--ground) 0%,var(--ground) 55%,var(--ground-deep) 100%)}
.brand{position:absolute;left:62px;top:10px;display:flex;align-items:center;gap:10px}
.brand-dot{width:50px;height:50px;border-radius:50%;background:var(--brand-blue)}
.brand-name{font-size:34px;font-weight:700;color:#333}
.main-nav{position:absolute;top:40px;left:551px;font-size:13px;letter-spacing:.2px}
.main-nav a{color:var(--nav);text-decoration:none;position:absolute;white-space:nowrap}
.page{position:absolute;left:104px;top:97px;width:812px;height:820px;background:var(--panel);border-radius:6px 6px 0 0;border:1px solid #cfcfcf}
.headline{position:absolute;top:40px;width:100%;text-align:center;font-family:"Archivo Black",sans-serif;font-size:40px;letter-spacing:1.5px;color:#2f2f2f;
  text-shadow:-2px -2px 0 #fff,2px -2px 0 #fff,-2px 2px 0 #fff,2px 2px 0 #fff,0 0 3px #999}
.subline{position:absolute;top:97px;width:100%;text-align:center;font-size:16px;letter-spacing:.6px;color:var(--muted)}
.intro{position:absolute;top:137px;width:100%;text-align:center;font-size:12px;letter-spacing:.45px;color:#444}
.map{position:absolute;left:65px;top:203px;width:369px;height:217px;background:var(--map);border:1px solid #d0d0d0;border-radius:4px}
.share{position:absolute;left:503px;top:212px;list-style:none}
.share li{display:flex;align-items:center;height:42px;font-size:12.5px;letter-spacing:.3px;color:#333}
.share span{width:24px;height:24px;border-radius:3px;margin-right:13px}
.address-label{position:absolute;left:100px;top:457px;font-size:12.5px;letter-spacing:.4px;color:#333}
.address-box{position:absolute;left:477px;top:445px;width:282px;height:29px;border:1px solid #c8c8c8;border-radius:4px}
.address-box svg{position:absolute;right:6px;top:7px}
.address-box i{position:absolute;right:25px;top:5px;height:18px;border-left:1px solid #ccc}
.code-label{position:absolute;left:21px;top:536px;font-size:12px;letter-spacing:.3px;color:#222}
.code{position:absolute;left:15px;top:553px;width:776px;height:126px;border:1px solid #aaa;padding:3px;font-family:"Cousine",monospace;font-size:12.4px;letter-spacing:1.05px;line-height:16px;color:#111;overflow-wrap:anywhere;word-break:normal;overflow:hidden}
.footer{position:absolute;top:782px;left:0;width:100%;font-size:11px;letter-spacing:.35px;color:#333}
.footer a{position:absolute;color:#333;text-decoration:none;white-space:nowrap}
.controls{position:absolute;left:916px;top:129px;width:230px;height:790px;background:var(--side);border:1px solid #cfcfcf;border-radius:0 6px 0 0}
.controls h2{position:absolute;left:28px;top:25px;font-size:16px;font-weight:400;color:#333}
.ctl{position:absolute;left:28px;font-size:12px;color:#333}
.ctl label{display:block;margin-bottom:7px}
.select{width:129px;height:18px;border:1px solid #888;background:#fff;font-size:12px;padding:1px 4px;position:relative}
.select::after{content:"";position:absolute;right:0;top:0;width:14px;height:16px;background:#ddd;border-left:1px solid #888}
.select b{position:absolute;right:3px;top:6px;border:4px solid transparent;border-top-color:#222;border-bottom:0;z-index:1}
.input{height:25px;border:1px solid #c6c6c6;background:#fff;font-size:12px;padding:5px 6px}
.radio{display:flex;gap:14px;font-size:12px}
.radio span::before{content:"";display:inline-block;width:8px;height:8px;border:1px solid #777;border-radius:50%;margin-right:5px;vertical-align:-1px}
.radio .on::before{background:radial-gradient(#222 40%,#fff 45%)}
.preview{position:absolute;left:17px;top:723px;width:111px;height:31px;border-radius:7px;background:#2a2a2a;box-shadow:0 0 0 2px #fff,0 0 0 3px #999;color:#fff;font-family:"Archivo Black",sans-serif;font-size:16px;text-align:center;line-height:31px;letter-spacing:.5px}
</style>
</head>
<body>
<div class="scenery" role="img" aria-label="Illustrated road with parked and driving cars framing the page"></div>

<div class="brand"><span class="brand-dot"></span><span class="brand-name">Kurbly</span></div>

<nav class="main-nav">
  <a style="left:0">Home</a>
  <a style="left:88px">Get Kurbly</a>
  <a style="left:217px">Widget</a>
  <a style="left:301px">Car Navigation</a>
  <a style="left:440px">About</a>
</nav>

<main class="page">
  <h1 class="headline">Throwing a Party ? Wedding ?</h1>
  <p class="subline">Concerned that no one will show up because they would never find parking by your place?</p>
  <p class="intro">Attach Kurbly Widget to your Friendsy or Invitely invitations, or post it on your Gatherly page, and make life easier for your guests!</p>
  <div class="map" role="img" aria-label="Street map of the neighbourhood around the event address"></div>
  <ul class="share">
    <li><span style="background:#8a8a8a"></span>PressLeaf Blog</li>
    <li><span style="background:#8fa8d0"></span>Friendsy</li>
    <li><span style="background:#8cc68a"></span>Invitely</li>
    <li><span style="background:#e88a80"></span>Gatherly</li>
  </ul>
  <p class="address-label">Enter an address to get your own Kurbly Widget</p>
  <div class="address-box"><i></i>
    <svg width="13" height="13" viewBox="0 0 13 13"><circle cx="7.5" cy="5.5" r="4" fill="none" stroke="#333" stroke-width="1.6"/><path d="M4.6 8.4 L1 12" stroke="#333" stroke-width="2"/></svg>
  </div>
  <p class="code-label">Get the Code</p>
  <div class="code">&lt;iframe allowTransparency='true' frameborder='0' scrolling='no' src='http://www.platemerio.com/widgets/sightings?background=EEEEEE&amp;border=CCCCCC&amp;border_radius=5&amp;height=192&amp;id=1&amp;image_border=regular&amp;image_border_width=10&amp;order=best&amp;page=1&amp;query=&amp;size=small&amp;type=place&amp;width=462&amp;x=4&amp;y=1' style='border:none; overflow:hidden; width:462px; height: 192px'&gt;&lt;/iframe&gt;</div>
  <footer class="footer">
    <a style="left:16px">About</a><a style="left:75px">Press</a><a style="left:136px">Jobs</a><a style="left:185px">Contact Us</a><a style="left:276px">Terms of Use</a><a style="left:385px">Privacy Policy</a><a style="left:606px">© 2012 Kurbly All Rights Reserved.</a>
  </footer>
</main>

<aside class="controls">
  <h2>Widget Controls</h2>
  <div class="ctl" style="top:61px"><label>Widget Type</label><div class="select">Wedding<b></b></div></div>
  <div class="ctl" style="top:126px"><label>Place Name</label><div class="input" style="width:129px">Dana &amp; Milos</div></div>
  <div class="ctl" style="top:198px"><label>Order By</label><div class="radio"><span class="on">Best</span><span>Latest</span></div></div>
  <div class="ctl" style="top:256px"><label>Image Size</label><div class="select">Small<b></b></div></div>
  <div class="ctl" style="top:322px"><label>Image Border</label><div class="select">Regular<b></b></div></div>
  <div class="ctl" style="top:388px"><label>Image Border width</label><div class="input" style="width:88px">1</div></div>
  <div class="ctl" style="top:454px"><label>Dimensions</label><div style="display:flex;align-items:center;gap:5px"><div class="input" style="width:43px">210</div>x<div class="input" style="width:43px">180</div></div></div>
  <div class="ctl" style="top:522px"><label>Background</label><div class="input" style="width:88px">333333</div></div>
  <div class="ctl" style="top:590px"><label>Border</label><div class="input" style="width:88px">000000</div></div>
  <div class="ctl" style="top:658px"><label>Border radius</label><div class="input" style="width:88px">5</div></div>
  <div class="preview">Preview</div>
</aside>
</body>
</html>
```